Kelbrook LLC web design project

Dallas, TX based water damage mitigation company needs a web site for its new business. The company does water extractions, mitigation, demo, restoration, and reconstruction. We need for the site to have a strong mobile version, and the owners/managers need to be able to edit the site despite having no web design experience. The site needs to look and function, especially the mobile version, similar to bramfieldorchardworks.com if possible.

```html
<!DOCTYPE html>
<html lang="en">
<head>
<meta charset="utf-8">
<title>Kelbrook LLC – Water Damage Mitigation</title>
<link href="https://fonts.googleapis.com/css2?family=Raleway:wght@300;400;600;700;800&family=Open+Sans:wght@400;600;700&display=swap" rel="stylesheet">
<style>
:root{
  --blue:#1b6fc2;
  --blue-dark:#155a9f;
  --navy:#1f2b3b;
  --navy-deep:#17212e;
  --ink:#2a2f36;
  --muted:#6b737d;
  --light:#f3f5f8;
  --white:#ffffff;
  --gold:#f5b301;
}
*{box-sizing:border-box;margin:0;padding:0}
html,body{width:1200px;height:4528px;overflow:hidden}
body{font-family:"Open Sans",Arial,sans-serif;color:var(--ink);background:var(--white);font-size:13px;line-height:1.55}
.section{position:relative;width:1200px;overflow:hidden}
.btn{display:inline-flex;align-items:center;gap:8px;background:var(--blue);color:var(--white);font-family:"Raleway",sans-serif;font-weight:700;font-size:11px;letter-spacing:.5px;text-transform:uppercase;padding:9px 20px;border-radius:20px;border:0}
.btn.dark{background:var(--navy)}
.btn.white{background:var(--white);color:var(--blue)}
.heading{font-family:"Raleway",sans-serif;font-weight:300;font-size:44px;letter-spacing:1px;text-transform:uppercase;color:var(--blue);text-align:center}
.divider{display:flex;justify-content:center;gap:5px;margin:8px 0 20px}
.divider span{width:6px;height:6px;border-radius:50%;background:var(--blue)}
.lead{text-align:center;color:var(--muted);max-width:820px;margin:0 auto;font-size:13px}
.ph{display:block}

/* top bar */
.topbar{height:34px;background:var(--blue-dark);color:var(--white);display:flex;justify-content:space-between;align-items:center;padding:0 36px;font-size:11px}
.topbar .phone{background:var(--white);color:var(--blue);font-weight:700;padding:3px 12px;border-radius:12px}
/* nav */
.nav{height:66px;background:var(--white);display:flex;align-items:center;justify-content:space-between;padding:0 36px;position:relative;z-index:3;box-shadow:0 2px 6px rgba(0,0,0,.08)}
.nav ul{display:flex;gap:30px;list-style:none;font-family:"Raleway",sans-serif;font-weight:700;font-size:11px;text-transform:uppercase;color:var(--navy)}
.nav li.active{color:var(--white);background:var(--blue);padding:6px 12px;border-radius:3px;margin:-6px 0}
.brand{position:absolute;left:50%;top:0;transform:translateX(-50%);width:200px;height:118px;background:var(--white);display:flex;flex-direction:column;align-items:center;justify-content:center;gap:8px;border-radius:0 0 10px 10px;box-shadow:0 4px 10px rgba(0,0,0,.1)}
.brand .mark{width:34px;height:34px;border-radius:50%;background:var(--blue)}
.brand .name{font-family:"Raleway",sans-serif;font-weight:800;font-size:24px;color:var(--navy)}
/* hero */
.hero{height:572px;background:linear-gradient(100deg,#e9eef3 0%,#d5dee7 45%,#c3cfda 100%)}
.hero .photo{position:absolute;inset:0}
.hero .copy{position:absolute;left:56px;top:180px;width:460px}
.hero .eyebrow{font-family:"Raleway",sans-serif;font-weight:700;font-size:22px;color:var(--navy)}
.hero h1{font-family:"Raleway",sans-serif;font-weight:800;font-size:44px;line-height:1.05;color:var(--blue);text-transform:uppercase;margin:6px 0 14px}
.hero p{font-size:13px;color:var(--ink)}
.zip{display:flex;gap:10px;margin-top:22px}
.zip .field{width:130px;height:34px;border-radius:17px;background:var(--white);border:1px solid #cfd6de;padding:0 14px;display:flex;align-items:center;color:var(--muted);font-size:11px}

/* services */
.services{height:620px;padding-top:90px}
.tiles{display:flex;margin-top:30px;height:256px}
.tile{flex:1;position:relative;display:flex;align-items:flex-end;justify-content:center;padding-bottom:36px;color:var(--white);font-family:"Raleway",sans-serif;font-weight:700;font-size:14px;text-transform:uppercase}
.tile .ph{position:absolute;inset:0}
.tile span{position:relative}
.tile.active{background:var(--blue);flex-direction:column;justify-content:center;align-items:center;padding:0 22px;text-align:center;gap:10px}
.tile.active p{font-family:"Open Sans",sans-serif;font-weight:400;font-size:11px;text-transform:none}
.tile.active .more{font-size:10px;border-bottom:1px solid var(--white)}
.center{display:flex;justify-content:center;margin-top:22px}

/* work for */
.workfor{height:476px;margin-top:36px;background:var(--blue)}
.workfor .photo{position:absolute;left:0;top:0;width:620px;height:476px;clip-path:polygon(0 0,86% 0,100% 50%,86% 100%,0 100%)}
.workfor .copy{position:absolute;left:680px;top:50px;width:470px;color:var(--white)}
.workfor h2{font-family:"Raleway",sans-serif;font-weight:300;font-size:42px;text-transform:uppercase}
.workfor h2 b{font-weight:300;color:#d7e7f7}
.item{display:flex;gap:16px;margin-top:26px}
.item svg{flex:none}
.item h3{font-family:"Raleway",sans-serif;font-weight:700;font-size:15px;text-transform:uppercase}
.item p{font-size:11px;opacity:.9}

/* story */
.story{height:420px;padding:68px 60px 0}
.story .copy{width:560px}
.story h2{font-family:"Raleway",sans-serif;font-weight:700;font-size:38px;color:var(--blue);text-transform:uppercase}
.story h2 b{color:var(--navy)}
.story h4{font-size:15px;margin:10px 0 8px;color:var(--navy)}
.story p{color:var(--muted);margin-bottom:10px}
.story .frame{position:absolute;right:60px;top:78px;width:500px;height:296px;background:var(--light)}
.story .frame .ph{position:absolute;left:22px;top:-16px;width:456px;height:290px}

/* cta band */
.cta{height:300px;margin-top:0}
.cta .band{position:absolute;left:60px;right:60px;top:0;height:290px;background:var(--blue);color:var(--white);text-align:center;padding-top:38px}
.cta h2{font-family:"Raleway",sans-serif;font-weight:300;font-size:40px;text-transform:uppercase}
.cta h2 b{font-weight:800}
.cta p{font-size:12px;max-width:700px;margin:12px auto 18px;opacity:.9}
.cta .van{position:absolute;left:-20px;bottom:-6px;width:260px;height:116px;border-radius:10px}

/* how */
.how{height:510px;padding-top:76px}
.steps{display:flex;justify-content:space-between;width:900px;margin:24px auto 0}
.step{width:260px;text-align:center}
.step .ring{position:relative;width:120px;height:120px;margin:0 auto 18px;border:2px solid #d6dde5;border-radius:50%;display:flex;align-items:center;justify-content:center}
.step .ring .ph{width:84px;height:84px;border-radius:50%}
.step .num{position:absolute;left:-4px;top:-4px;width:30px;height:30px;border-radius:50%;background:var(--navy);color:var(--white);font-weight:700;font-size:13px;display:flex;align-items:center;justify-content:center}
.step h3{font-family:"Raleway",sans-serif;font-weight:700;font-size:16px;color:var(--blue)}
.step p{font-size:11px;color:var(--muted);margin-top:6px}

/* areas */
.areas{height:460px;background:#e7ecf1}
.areas .map{position:absolute;right:0;top:0;width:640px;height:460px}
.areas .panel{position:absolute;left:0;top:0;width:720px;height:460px;background:var(--blue);clip-path:polygon(0 0,80% 0,100% 50%,80% 100%,0 100%);padding:60px 0 0 60px;color:var(--white)}
.areas h2{font-family:"Raleway",sans-serif;font-weight:300;font-size:42px;text-transform:uppercase}
.areas .lead2{font-size:11px;width:440px;opacity:.9;margin:8px 0 20px}
.cities{display:grid;grid-template-columns:repeat(3,150px);gap:12px 0;font-size:11px;font-weight:600;margin-bottom:24px}
.cities div{display:flex;align-items:center;gap:7px}

/* testimonials */
.testimonials{height:528px;padding-top:72px}
.quotes{display:flex;justify-content:center;gap:36px;margin-top:44px}
.quote{width:340px;text-align:center;position:relative;padding-top:50px}
.quote .face{position:absolute;left:50%;top:-40px;transform:translateX(-50%);width:80px;height:80px;border-radius:50%;border:4px solid var(--white);box-shadow:0 2px 6px rgba(0,0,0,.15)}
.quote p{font-style:italic;color:var(--muted);font-size:12px}
.quote h4{color:var(--blue);font-family:"Raleway",sans-serif;font-size:15px;margin-top:12px}
.stars{color:var(--gold);letter-spacing:2px;font-size:13px}

/* locate */
.locate{height:124px;background:var(--blue);margin:0 60px;width:1080px;display:flex;align-items:center;justify-content:center;gap:24px;color:var(--white)}
.locate h2{font-family:"Raleway",sans-serif;font-weight:300;font-size:28px;text-transform:uppercase}
.locate .field{width:200px;height:34px;border-radius:17px;background:var(--white);padding:0 14px;display:flex;align-items:center;color:var(--muted);font-size:11px}
.locate-wrap{height:134px;background:linear-gradient(var(--white) 0 50%,var(--navy) 50%)}

/* footer */
.footer{height:286px;background:var(--navy);color:#c8d0da;display:flex;padding:40px 60px 0;gap:60px}
.footer .fbrand{width:220px}
.fbrand .name{font-family:"Raleway",sans-serif;font-weight:800;font-size:24px;color:var(--white);display:flex;align-items:center;gap:10px}
.fbrand .name i{width:28px;height:28px;border-radius:50%;background:var(--blue);display:block}
.socials{display:flex;gap:8px;margin-top:18px}
.socials span{width:26px;height:26px;border-radius:50%;background:var(--blue)}
.footer h5{font-family:"Raleway",sans-serif;font-weight:700;font-size:15px;color:var(--white);text-transform:uppercase;margin-bottom:12px}
.footer ul{list-style:none;font-size:12px;line-height:1.9}
.footer .col{width:170px}
.footer .contact{width:260px}
.contact li{display:flex;gap:8px;align-items:flex-start}
.bottom{height:38px;background:var(--navy-deep);color:#9aa5b2;font-size:11px;display:flex;align-items:center;justify-content:center}
</style>
</head>
<body>

<header class="section">
  <div class="topbar">
    <span>Welcome to Kelbrook LLC – We are here to help you 24/7</span>
    <span class="phone">(214) 555-0147</span>
  </div>
  <nav class="nav">
    <ul><li class="active">Home</li><li>About</li><li>Services</li><li>Service Areas</li></ul>
    <div class="brand"><span class="mark"></span><span class="name">Kelbrook LLC</span></div>
    <ul><li>Why Us</li><li>Testimonials</li><li>Blog</li><li>Contact</li></ul>
  </nav>
</header>

<section class="section hero">
  <div class="photo ph" role="img" aria-label="Technician in uniform holding a tablet beside a white service van, house in the background" style="background:linear-gradient(100deg,rgba(240,244,248,.95) 0%,rgba(228,235,242,.8) 40%,#b9c6d3 62%,#8797a8 100%)"></div>
  <div class="copy">
    <div class="eyebrow">24/7 DALLAS, TEXAS</div>
    <h1>Water Damage<br>Mitigation</h1>
    <p>Fast response for flooded homes and offices. Our crew arrives quickly, removes standing water and dries every room to keep damage small.</p>
    <div class="zip"><span class="field">Enter Zip Code</span><span class="btn">
      <svg width="10" height="12" viewBox="0 0 10 12"><path d="M5 0a4 4 0 0 0-4 4c0 3 4 8 4 8s4-5 4-8a4 4 0 0 0-4-4z" fill="#fff"/></svg>Find Location</span></div>
  </div>
</section>

<section class="section services">
  <h2 class="heading">Our Services</h2>
  <div class="divider"><span></span><span></span><span></span></div>
  <p class="lead">From the first call to the final repair, we handle every stage of water damage work with trained crews, modern drying gear and clear updates along the way.</p>
  <div class="tiles">
    <div class="tile"><span class="ph" role="img" aria-label="Water extraction equipment on a wet floor" style="background:linear-gradient(#7d8a97,#3e4a57)"></span><span>Water Extractions</span></div>
    <div class="tile"><span class="ph" role="img" aria-label="Drying fans in a flooded room" style="background:linear-gradient(#8f9ba6,#4a5662)"></span><span>Water Mitigation</span></div>
    <div class="tile active"><span>Demolition</span><p>Careful removal of soaked walls, floors and fixtures so the space can dry fully and safely.</p><span class="more">Read More</span></div>
    <div class="tile"><span class="ph" role="img" aria-label="Restored interior room" style="background:linear-gradient(#9aa4ad,#566270)"></span><span>Restoration</span></div>
    <div class="tile"><span class="ph" role="img" aria-label="Reconstruction work with new drywall" style="background:linear-gradient(#a3a9b0,#5d6874)"></span><span>Reconstruction</span></div>
  </div>
  <div class="center"><span class="btn dark">View All Services</span></div>
</section>

<section class="section workfor">
  <div class="photo ph" role="img" aria-label="Technician shaking hands with a homeowner at a front door" style="background:linear-gradient(120deg,#cfd7df,#8e9aa6)"></div>
  <div class="copy">
    <h2>We <b>Work For</b></h2>
    <div class="item">
      <svg width="44" height="44" viewBox="0 0 44 44" fill="none" stroke="#fff" stroke-width="2"><rect x="8" y="8" width="18" height="32"/><rect x="26" y="18" width="12" height="22"/><path d="M13 14h3M19 14h3M13 21h3M19 21h3M13 28h3M19 28h3"/></svg>
      <div><h3>Commercial Property Owners</h3><p>We restore offices, shops and warehouses fast so your business can reopen with less downtime.</p></div>
    </div>
    <div class="item">
      <svg width="44" height="44" viewBox="0 0 44 44" fill="none" stroke="#fff" stroke-width="2"><path d="M6 22 22 8l16 14"/><path d="M11 18v20h22V18"/><rect x="19" y="27" width="7" height="11"/></svg>
      <div><h3>Residential Property</h3><p>Homeowners get caring help, careful drying and full repairs for every room affected by water.</p></div>
    </div>
    <div class="item">
      <svg width="44" height="44" viewBox="0 0 44 44" fill="none" stroke="#fff" stroke-width="2"><rect x="8" y="6" width="24" height="32" rx="2"/><path d="M13 14h14M13 20h14M13 26h9"/><circle cx="32" cy="32" r="6"/></svg>
      <div><h3>Insurance Company</h3><p>Detailed photos, moisture logs and clear reports make every claim simple to review and approve.</p></div>
    </div>
  </div>
</section>

<section class="section story">
  <div class="copy">
    <h2><b>Kelbrook</b> Story</h2>
    <h4>Providing the Peace of Mind You Deserve.</h4>
    <p>Kelbrook LLC was founded in Dallas by a team that saw too many families wait days for help after a leak or flood. We built a crew that answers at any hour and shows up ready to work.</p>
    <p>Each job is planned with care, from water removal to the last coat of paint, so you always know what comes next.</p>
    <span class="btn" style="margin-top:8px">Read More</span>
  </div>
  <div class="frame"><span class="ph" role="img" aria-label="Dallas city skyline at night" style="background:linear-gradient(#0e1a33,#2b3c63 70%,#6b5a3a)"></span></div>
</section>

<section class="section cta">
  <div class="band">
    <h2>Here For You <b>Every Step</b> Of The Way</h2>
    <p>Call our team any time of day. We answer, assess and start drying right away so small leaks never turn into big repairs.</p>
    <span class="btn white">
      <svg width="11" height="11" viewBox="0 0 24 24"><path d="M6.6 10.8a15 15 0 0 0 6.6 6.6l2.2-2.2c.3-.3.7-.4 1-.2 1.1.4 2.3.6 3.6.6.6 0 1 .4 1 1V20c0 .6-.4 1-1 1A17 17 0 0 1 3 4c0-.6.4-1 1-1h3.5c.6 0 1 .4 1 1 0 1.3.2 2.5.6 3.6.1.3 0 .7-.2 1z" fill="#1b6fc2"/></svg>Contact Us Today</span>
    <span class="van ph" role="img" aria-label="White company service van" style="background:linear-gradient(#f4f6f8,#cfd6dd)"></span>
  </div>
</section>

<section class="section how">
  <h2 class="heading">How It Works</h2>
  <div class="divider"><span></span><span></span><span></span></div>
  <div class="steps">
    <div class="step"><div class="ring"><span class="num">1</span><span class="ph" role="img" aria-label="Illustration of a person on a phone call" style="background:#dbe8f5"></span></div><h3>Call Us Today</h3><p>Tell us what happened and where. A team member picks up at any hour and books a visit.</p></div>
    <div class="step"><div class="ring"><span class="num">2</span><span class="ph" role="img" aria-label="Illustration of a building being inspected" style="background:#dbe8f5"></span></div><h3>We Assess Your Situation</h3><p>Our tech measures moisture, finds the source and explains the plan before work starts.</p></div>
    <div class="step"><div class="ring"><span class="num">3</span><span class="ph" role="img" aria-label="Illustration of a technician with tools" style="background:#dbe8f5"></span></div><h3>We Help You Restore</h3><p>We dry, clean and rebuild until your property looks and feels like home again.</p></div>
  </div>
  <div class="center" style="margin-top:26px"><span class="btn dark">Call Us Now</span></div>
</section>

<section class="section areas">
  <span class="map ph" role="img" aria-label="Street map of the Dallas area" style="background:linear-gradient(135deg,#e8ebe4,#d3dbe3)"></span>
  <div class="panel">
    <h2>Service Areas</h2>
    <p class="lead2">We proudly serve Dallas and the nearby towns across the metro area with round-the-clock response.</p>
    <div class="cities">
      <div>📍Downtown</div><div>📍Uptown</div><div>📍Oak Cliff</div>
      <div>📍Garland</div><div>📍Irving</div><div>📍Mesquite</div>
      <div>📍Plano</div><div>📍Richardson</div><div>📍Carrollton</div>
    </div>
    <span class="btn dark">Learn More</span>
  </div>
</section>

<section class="section testimonials">
  <h2 class="heading">Clients Testimonials</h2>
  <div class="divider"><span></span><span></span><span></span></div>
  <div class="quotes">
    <div class="quote"><span class="face ph" role="img" aria-label="Customer portrait" style="background:#c9b6a4"></span><p>"They arrived within an hour of my call and had the basement dry in two days. Friendly, honest and very thorough from start to end."</p><h4>Marcus Hale</h4><div class="stars">★★★★★</div></div>
    <div class="quote"><span class="face ph" role="img" aria-label="Customer portrait" style="background:#d3b9a8"></span><p>"The crew explained every step and worked directly with my insurer. Our kitchen looks better now than before the pipe burst."</p><h4>Priya Lane</h4><div class="stars">★★★★★</div></div>
    <div class="quote"><span class="face ph" role="img" aria-label="Customer portrait" style="background:#c7a593"></span><p>"Quick, tidy and fair pricing. I would call this team again without a second thought and recommend them to any neighbor."</p><h4>Evan Ross</h4><div class="stars">★★★★★</div></div>
  </div>
</section>

<div class="section locate-wrap">
  <div class="locate">
    <svg width="30" height="36" viewBox="0 0 10 12"><path d="M5 0a4 4 0 0 0-4 4c0 3 4 8 4 8s4-5 4-8a4 4 0 0 0-4-4zm0 5.6A1.6 1.6 0 1 1 5 2.4a1.6 1.6 0 0 1 0 3.2z" fill="#fff"/></svg>
    <h2>Find Your Location</h2>
    <span class="field">Enter Zip Code</span>
    <span class="btn dark">Find</span>
  </div>
</div>

<footer class="section">
  <div class="footer">
    <div class="fbrand">
      <div class="name"><i></i>Kelbrook LLC</div>
      <div class="socials"><span></span><span></span><span></span><span></span></div>
    </div>
    <div class="col"><h5>Useful Links</h5><ul><li>About</li><li>Services</li><li>Service Areas</li><li>Why Us</li><li>Testimonials</li><li>Blog</li><li>Contact</li></ul></div>
    <div class="col"><h5>Services</h5><ul><li>Water Extractions</li><li>Water Mitigation</li><li>Demolition</li><li>Restoration</li><li>Reconstruction</li></ul></div>
    <div class="contact"><h5>Contact Us</h5><ul>
      <li>📍 48 Ridgeline Ave, Dallas, TX 75201</li>
      <li>📞 (214) 555-0147</li>
      <li>✉ info@bramfieldorchardworks.com</li></ul></div>
  </div>
  <div class="bottom">© Kelbrook LLC – 2024. All Rights Reserved.</div>
</footer>

</body>
</html>
```